"Eid Celebration" Islamic Flyer

Hi,

We need an Islamic Flyer done for our annual 'Eid Celebration' (A3 Portrait).

I have attached last years 'Eid Flyer [login to view URL]' with the layout and information we need.

Please create a brand new, and fresh design, but with all the same information on the flyer:
_______________________________________________

(BQMTE Logo)

Eid Celebration

(Tag) All welcome!

Wednesday 5th August
12 - 5pm
Fernway Court
- University of Brantholme

Free BBQ + Sweets! ^_^

Proud Sponsors:

University of Brantholme Logo
Omar's Halal butcher Logo
Brantholme University Union Logo
Dar Kovo Logo

____________________

I have attached the logo's required on this years Flyer.

I have also attached some Design Idea's.

Note: We only want a Light colored flyer (White/Blue, Orange, Green, etc.)

Thank you,

```html
<!DOCTYPE html>
<html lang="en">
<head>
<meta charset="utf-8">
<title>Eid Celebration – BQMTE</title>
<link href="https://fonts.googleapis.com/css2?family=Montserrat:wght@800&family=Open+Sans:wght@400;700&family=Pinyon+Script&display=swap" rel="stylesheet">
<style>
  :root {
    --green-deep: #23913f;
    --green-mid: #35a24c;
    --green-pale: #8cc58d;
    --green-sky: #a9d2a6;
    --column: #b9dbb4;
    --cream: #f4efd8;
    --yellow: #f2e81c;
    --red: #b3201f;
    --red-dark: #8e1515;
    --orange: #f0a022;
    --white: #ffffff;
    --ink: #333333;
    --navy: #1d2d5a;
    --sponsor-red: #d0202a;
    --sponsor-orange: #e8713a;
  }
  html, body {
    margin: 0;
    padding: 0;
    overflow: hidden;
    background: #ffffff;
  }
  .flyer {
    position: relative;
    width: 847px;
    height: 1200px;
    overflow: hidden;
    background: linear-gradient(180deg, var(--green-sky) 0%, var(--green-pale) 40%, var(--green-mid) 100%);
    font-family: "Open Sans", Arial, sans-serif;
  }
  .flyer__backdrop {
    position: absolute;
    inset: 0;
    width: 847px;
    height: 1200px;
  }
  .skyline {
    position: absolute;
    left: 150px;
    top: 140px;
    width: 547px;
    height: 520px;
    background: linear-gradient(180deg, rgba(20, 110, 45, 0.0) 0%, rgba(20, 110, 45, 0.22) 45%, rgba(20, 110, 45, 0.0) 100%);
  }
  .brand {
    position: absolute;
    top: 82px;
    left: 0;
    width: 847px;
    display: flex;
    justify-content: center;
    align-items: center;
    gap: 10px;
  }
  .brand__dot {
    width: 26px;
    height: 26px;
    border-radius: 50%;
    background: var(--white);
  }
  .brand__name {
    font-family: "Open Sans", Arial, sans-serif;
    font-weight: 700;
    font-size: 40px;
    color: var(--white);
    letter-spacing: 1px;
  }
  .title {
    position: absolute;
    top: 270px;
    left: 0;
    width: 847px;
    text-align: center;
    margin: 0;
    color: var(--cream);
  }
  .title__script {
    display: block;
    font-family: "Pinyon Script", cursive;
    font-weight: 400;
    font-size: 138px;
    line-height: 140px;
    text-shadow: 0 3px 6px rgba(0, 0, 0, 0.25);
  }
  .title__main {
    display: block;
    font-family: "Montserrat", Arial, sans-serif;
    font-weight: 800;
    font-size: 78px;
    line-height: 86px;
    margin-top: -8px;
    text-shadow: 0 4px 6px rgba(0, 0, 0, 0.35);
  }
  .tagline {
    position: absolute;
    top: 524px;
    left: 0;
    width: 847px;
    display: flex;
    justify-content: center;
    align-items: center;
    gap: 14px;
  }
  .tagline__rule {
    width: 62px;
    height: 3px;
    border-top: 1px solid var(--yellow);
    border-bottom: 1px solid var(--yellow);
  }
  .tagline__text {
    font-family: "Pinyon Script", cursive;
    font-size: 48px;
    color: var(--yellow);
    line-height: 60px;
  }
  .details {
    position: absolute;
    top: 590px;
    left: 0;
    width: 847px;
    text-align: center;
    color: var(--yellow);
    font-size: 28px;
    line-height: 48px;
    margin: 0;
  }
  .details strong { font-weight: 700; }
  .divider {
    position: absolute;
    top: 728px;
    left: 185px;
    width: 477px;
    height: 20px;
  }
  .offer {
    position: absolute;
    top: 804px;
    left: 165px;
    width: 519px;
    height: 78px;
    border-radius: 8px;
    background: linear-gradient(180deg, var(--red) 0%, var(--red-dark) 100%);
    box-shadow: 0 14px 18px rgba(0, 0, 0, 0.25);
    display: flex;
    align-items: center;
    justify-content: center;
    gap: 30px;
    color: var(--white);
    font-size: 33px;
  }
  .offer strong { font-weight: 700; }
  .offer__smile { width: 38px; height: 38px; }
  .sponsors__label {
    position: absolute;
    top: 1006px;
    left: 34px;
    margin: 0;
    font-size: 25px;
    font-weight: 400;
    color: var(--ink);
  }
  .sponsors__list {
    position: absolute;
    top: 1068px;
    left: 30px;
    width: 790px;
    margin: 0;
    padding: 0;
    list-style: none;
    display: flex;
    justify-content: space-between;
    align-items: center;
  }
  .sponsor {
    display: flex;
    align-items: center;
    gap: 8px;
    font-family: "Open Sans", Arial, sans-serif;
    font-weight: 700;
    font-size: 19px;
    line-height: 22px;
  }
  .sponsor__mark { width: 22px; height: 22px; flex: none; }
  .sponsor--university { color: var(--navy); }
  .sponsor--university .sponsor__mark { background: var(--navy); }
  .sponsor--butcher { color: var(--sponsor-red); }
  .sponsor--union { color: var(--sponsor-red); }
  .sponsor--union .sponsor__mark { background: var(--sponsor-red); }
  .sponsor--kitchen { color: var(--sponsor-orange); }
  .sponsor--kitchen .sponsor__mark { background: var(--sponsor-orange); border-radius: 50%; }
</style>
</head>
<body>
<main class="flyer">
  <svg class="flyer__backdrop" viewBox="0 0 847 1200" aria-hidden="true">
    <defs>
      <linearGradient id="panelFill" x1="0" y1="0" x2="0" y2="1">
        <stop offset="0" stop-color="#2d9b47"/>
        <stop offset="1" stop-color="#1f8b3a"/>
      </linearGradient>
      <linearGradient id="columnFill" x1="0" y1="0" x2="1" y2="0">
        <stop offset="0" stop-color="#cfe7c9"/>
        <stop offset="0.5" stop-color="#a8d2a2"/>
        <stop offset="1" stop-color="#cfe7c9"/>
      </linearGradient>
    </defs>
    <path class="arch" d="M42 1100 V300 C42 140 250 45 423 45 C596 45 804 140 804 300 V1100 Z" fill="url(#panelFill)"/>
    <rect class="column" x="6" y="300" width="44" height="700" fill="url(#columnFill)"/>
    <rect class="column__cap" x="0" y="287" width="56" height="22" fill="#f3f0dc"/>
    <rect class="column" x="797" y="300" width="44" height="700" fill="url(#columnFill)"/>
    <rect class="column__cap" x="791" y="287" width="56" height="22" fill="#f3f0dc"/>
    <path class="wave__accent" d="M300 1005 C520 995 700 935 847 860 V965 C700 1000 560 1012 300 1005 Z" fill="#f0a022"/>
    <path class="wave" d="M0 905 C120 860 250 880 370 935 C490 990 660 1000 847 905 V1200 H0 Z" fill="#ffffff"/>
  </svg>

  <div class="skyline" role="img" aria-label="Faint mosque domes and minarets silhouette"></div>

  <header class="brand">
    <span class="brand__dot"></span>
    <span class="brand__name">BQMTE</span>
  </header>

  <h1 class="title">
    <span class="title__script">Eid</span>
    <span class="title__main">CELEBRATION</span>
  </h1>

  <div class="tagline">
    <span class="tagline__rule"></span>
    <span class="tagline__text">All welcome</span>
    <span class="tagline__rule"></span>
  </div>

  <p class="details">
    WEDNESDAY <strong>5TH</strong> AUGUST | <strong>12 - 5PM</strong><br>
    <strong>FERNWAY COURT</strong> -<br>
    UNIVERSITY OF BRANTHOLME
  </p>

  <svg class="divider" viewBox="0 0 477 20" aria-hidden="true">
    <line x1="0" y1="6" x2="205" y2="6" stroke="#f2e81c" stroke-width="1.5"/>
    <line x1="0" y1="10" x2="205" y2="10" stroke="#f2e81c" stroke-width="1.5"/>
    <line x1="272" y1="6" x2="477" y2="6" stroke="#f2e81c" stroke-width="1.5"/>
    <line x1="272" y1="10" x2="477" y2="10" stroke="#f2e81c" stroke-width="1.5"/>
    <circle cx="238" cy="8" r="6" fill="#f2e81c"/>
  </svg>

  <div class="offer">
    <span><strong>FREE</strong> BBQ + SWEETS!</span>
    <svg class="offer__smile" viewBox="0 0 38 38" aria-hidden="true">
      <path d="M5 22 C10 34 28 34 34 20" fill="none" stroke="#ffffff" stroke-width="3.5" stroke-linecap="round"/>
      <line x1="14" y1="8" x2="15" y2="16" stroke="#ffffff" stroke-width="3.5" stroke-linecap="round"/>
      <line x1="22" y1="8" x2="23" y2="16" stroke="#ffffff" stroke-width="3.5" stroke-linecap="round"/>
    </svg>
  </div>

  <section class="sponsors">
    <h2 class="sponsors__label">Proud Sponsors:</h2>
    <ul class="sponsors__list">
      <li class="sponsor sponsor--university"><span class="sponsor__mark"></span>University of<br>Brantholme</li>
      <li class="sponsor sponsor--butcher">Omar's<br>Halal butcher</li>
      <li class="sponsor sponsor--union"><span class="sponsor__mark"></span>Brantholme<br>University Union</li>
      <li class="sponsor sponsor--kitchen"><span class="sponsor__mark"></span>Dar Kovo</li>
    </ul>
  </section>
</main>
</body>
</html>
```